Quotation (Proposal) Form

We are looking for a redesign of an existing form - one that fits our new marketing material better and, frankly, a form that looks a lot nicer than the boring form we use today. 8.5"x11". CMYK. Minimum 300 dpi necessary for printing. I have attached our current quote form as well as some other designs that show the direction we are going in. Please note, that this has to be able to have our people manually write in pen on it when we provide it to potential customers. Thank you!

Target Market(s)

Residential homeowners

Industry/Entity Type

Snow Removal

Font styles to use
Sans Serif

Colors

Designer to choose colors to be used in the design.

Requirements
Must have
• Should be easy to read and look great. Should also add the following text - "Exclusively serving Northeast Grand Rapids and suburbs"
Nice to have
• Similar concept to other marketing material we have done (attached). Easy to read. Professional.
Should not have
• Cluttered look. Unevenly spaced.

```html
<!DOCTYPE html>
<html lang="en">
<head>
<meta charset="utf-8">
<title>Ridgeline Snowplowing – Seasonal Quote Form</title>
<link href="https://fonts.googleapis.com/css2?family=Montserrat:wght@600;700&family=Open+Sans:ital,wght@0,600;0,700;1,700&display=swap" rel="stylesheet">
<style>
  :root {
    --backdrop: #d6d6d8;
    --paper: #ffffff;
    --ink: #111111;
    --label: #555555;
    --body: #3a3a3a;
    --band-from: #e6e6e8;
    --band-to: #f6f6f7;
    --field: #f0f0f1;
    --badge: #8d8d90;
    --badge-dark: #6d6d70;
  }
  * { box-sizing: border-box; margin: 0; padding: 0; }
  html, body { width: 1200px; height: 1000px; overflow: hidden; }
  body {
    background: var(--backdrop);
    font-family: "Open Sans", Arial, sans-serif;
    color: var(--body);
    position: relative;
  }
  .sheet {
    position: absolute; left: 262px; top: 64px;
    width: 673px; height: 871px;
    background: var(--paper);
    box-shadow: 4px 6px 14px rgba(0,0,0,.25);
    overflow: hidden;
  }
  .road-scene {
    position: absolute; left: 0; top: 470px; width: 673px; height: 330px;
    background: linear-gradient(180deg, rgba(230,230,232,0) 0%, rgba(222,222,224,.7) 45%, rgba(235,235,237,.9) 80%, rgba(255,255,255,0) 100%);
  }
  .field {
    position: absolute; left: 0; height: 39px;
    background: linear-gradient(90deg, var(--band-from), var(--band-to));
  }
  .field .tab {
    position: absolute; left: 0; top: 0; width: 12px; height: 39px;
  }
  .field .label {
    position: absolute; left: 30px; top: 13px;
    font: 700 14px/1 "Open Sans", Arial, sans-serif;
    color: var(--label); letter-spacing: .3px;
  }
  .field.zip { left: 246px; }
  .field.zip .label { left: 26px; top: 16px; }
  .brand-seal {
    position: absolute; left: 418px; top: 80px; width: 232px; height: 232px;
    border-radius: 50%; background: var(--paper);
    box-shadow: 0 0 6px rgba(0,0,0,.25);
    display: flex; flex-direction: column; align-items: center; justify-content: center; gap: 6px;
  }
  .brand-seal .mark { width: 20px; height: 20px; border-radius: 50%; background: var(--ink); }
  .brand-seal .name {
    font: 700 24px/1.15 "Open Sans", Arial, sans-serif; color: var(--ink); text-align: center;
  }
  .service-title {
    position: absolute; left: 24px; top: 346px;
    font: 700 23px/1 "Montserrat", Arial, sans-serif; color: var(--ink); letter-spacing: .5px;
  }
  .rule-pair { position: absolute; left: 24px; width: 182px; }
  .rule-pair span { display: block; background: var(--ink); }
  .rule-pair .thick { height: 7px; }
  .rule-pair .thin { height: 3px; margin-top: 4px; }
  .quote-title {
    position: absolute; left: 24px; top: 414px;
    font: 700 32px/32px "Montserrat", Arial, sans-serif; color: var(--ink);
  }
  .contact { position: absolute; left: 26px; top: 592px; list-style: none; }
  .contact li {
    display: flex; align-items: flex-start; gap: 9px;
    font: 600 11px/15px "Open Sans", Arial, sans-serif; color: var(--body);
    margin-bottom: 13px;
  }
  .contact svg { width: 19px; height: 15px; flex: none; }
  .checklist { position: absolute; left: 246px; top: 350px; width: 400px; list-style: none; }
  .checklist li {
    position: relative; padding-left: 22px; margin-bottom: 8px;
    font: 600 10.6px/13px "Open Sans", Arial, sans-serif; color: var(--body);
  }
  .checklist svg { position: absolute; left: 0; top: 0; width: 15px; height: 13px; }
  .payment-rule { position: absolute; left: 246px; top: 636px; width: 408px; height: 10px; background: var(--ink); }
  .payment-rule::after { content: ""; position: absolute; left: 0; top: 12px; width: 100%; height: 2px; background: var(--ink); }
  .payment {
    position: absolute; left: 246px;
    font: italic 700 11px/1 "Open Sans", Arial, sans-serif; color: var(--ink);
  }
  .pay-box {
    position: absolute; height: 20px; background: var(--field);
    border-radius: 3px; box-shadow: 0 0 3px rgba(0,0,0,.25);
  }
  .sign-card {
    position: absolute; left: 29px; top: 758px; width: 317px; height: 85px;
    background: var(--paper); border-radius: 12px;
    box-shadow: 0 1px 6px rgba(0,0,0,.35);
    padding: 12px 16px 0 18px;
  }
  .sign-card h2 { font: italic 700 12px/1 "Open Sans", Arial, sans-serif; color: var(--ink); margin-bottom: 12px; }
  .sign-row { display: flex; font: 700 10.5px/1 "Open Sans", Arial, sans-serif; color: var(--ink); margin-bottom: 8px; }
  .sign-row .who { width: 74px; }
  .sign-row .line { border-bottom: 1px solid var(--ink); }
  .sign-row .sig { width: 104px; margin-right: 14px; }
  .sign-row .date { width: 62px; }
  .sign-row .dl { margin-right: 2px; }
  .service-area {
    position: absolute; left: 358px; top: 774px;
    font: 600 11px/1 "Open Sans", Arial, sans-serif; color: var(--label);
  }
  .badges { position: absolute; left: 378px; top: 804px; display: flex; gap: 30px; }
  .badges svg { width: 48px; height: 52px; }
</style>
</head>
<body>
<main class="sheet">
  <div class="road-scene" role="img" aria-label="Faint winter photo of a snowy road stretching into the distance"></div>

  <div class="field" style="top:59px;width:468px"><svg class="tab" viewBox="0 0 12 39"><path d="M0 0H6L12 19.5 6 39H0Z" fill="#111"/></svg><span class="label">NAME</span></div>
  <div class="field" style="top:107px;width:468px"><svg class="tab" viewBox="0 0 12 39"><path d="M0 0H6L12 19.5 6 39H0Z" fill="#111"/></svg><span class="label" style="left:28px;top:11px">ADDRESS</span></div>
  <div class="field" style="top:156px;width:468px"><svg class="tab" viewBox="0 0 12 39"><path d="M0 0H6L12 19.5 6 39H0Z" fill="#111"/></svg><span class="label">PHONE</span></div>
  <div class="field" style="top:204px;width:240px"><svg class="tab" viewBox="0 0 12 39"><path d="M0 0H6L12 19.5 6 39H0Z" fill="#111"/></svg><span class="label">CITY</span></div>
  <div class="field zip" style="top:204px;width:222px"><svg class="tab" viewBox="0 0 12 39"><path d="M0 0H6L12 19.5 6 39H0Z" fill="#111"/></svg><span class="label">ZIP</span></div>
  <div class="field" style="top:253px;width:468px"><svg class="tab" viewBox="0 0 12 39"><path d="M0 0H6L12 19.5 6 39H0Z" fill="#111"/></svg><span class="label" style="left:29px">EMAIL ADDRESS</span></div>

  <div class="brand-seal">
    <span class="mark"></span>
    <span class="name">Ridgeline<br>Snowplowing</span>
  </div>

  <h1 class="service-title">SNOWPLOWING</h1>
  <div class="rule-pair" style="top:386px"><span class="thick"></span><span class="thin"></span></div>
  <h2 class="quote-title">Unlimited<br>Plowing<br>Seasonal<br>Quote</h2>
  <div class="rule-pair" style="top:558px"><span class="thick"></span><span class="thin"></span></div>

  <ul class="contact">
    <li><svg viewBox="0 0 19 15"><path d="M1 5C4 1 15 1 18 5L15 6.5 13 4.5H6L4 6.5Z M4 8H15L17 14H2Z" fill="#111"/><circle cx="9.5" cy="10.5" r="2" fill="#fff"/></svg>(555) 014-2276</li>
    <li><svg viewBox="0 0 19 15"><rect x="2" y="2" width="15" height="11" fill="#111"/><path d="M2 2.5 9.5 8 17 2.5" fill="none" stroke="#fff" stroke-width="1.2"/></svg>office@ridgelinesnow.com</li>
    <li><svg viewBox="0 0 19 15"><g fill="none" stroke="#111" stroke-width="1.3"><circle cx="9.5" cy="7.5" r="6.5"/><ellipse cx="9.5" cy="7.5" rx="3" ry="6.5"/><path d="M3 7.5H16M4 4H15M4 11H15"/></g></svg>ridgelinesnow.com</li>
    <li><svg viewBox="0 0 19 15"><path d="M9.5 15C5 9 4 7.5 4 5.5A5.5 5.5 0 0 1 15 5.5C15 7.5 14 9 9.5 15Z" fill="#111"/><circle cx="9.5" cy="5.5" r="2" fill="#fff"/></svg>1840 Birchwood Lane<br>NE, Grand Rapids<br>MI 49500</li>
  </ul>

  <ul class="checklist">
    <li><svg viewBox="0 0 15 13"><path d="M1 7 5 11 14 1" fill="none" stroke="#111" stroke-width="2"/></svg>Ridgeline is a fully licensed and insured snow removal service.</li>
    <li><svg viewBox="0 0 15 13"><path d="M1 7 5 11 14 1" fill="none" stroke="#111" stroke-width="2"/></svg>Plowing will be done when snow has accumulated 1" or more.</li>
    <li><svg viewBox="0 0 15 13"><path d="M1 7 5 11 14 1" fill="none" stroke="#111" stroke-width="2"/></svg>24 hour phone availability during snow events.</li>
    <li><svg viewBox="0 0 15 13"><path d="M1 7 5 11 14 1" fill="none" stroke="#111" stroke-width="2"/></svg>Hard rubber plow edges protect concrete and pavement from scratches and rust marks.</li>
    <li><svg viewBox="0 0 15 13"><path d="M1 7 5 11 14 1" fill="none" stroke="#111" stroke-width="2"/></svg>Snow will be removed by 6:00 am depending upon time and amount.</li>
    <li><svg viewBox="0 0 15 13"><path d="M1 7 5 11 14 1" fill="none" stroke="#111" stroke-width="2"/></svg>Hand shoveling of walkways/front patios available.</li>
    <li><svg viewBox="0 0 15 13"><path d="M1 7 5 11 14 1" fill="none" stroke="#111" stroke-width="2"/></svg>Salting of driveways available.</li>
    <li><svg viewBox="0 0 15 13"><path d="M1 7 5 11 14 1" fill="none" stroke="#111" stroke-width="2"/></svg>We will return to clean the approch of your drive after the city plows your street.</li>
    <li><svg viewBox="0 0 15 13"><path d="M1 7 5 11 14 1" fill="none" stroke="#111" stroke-width="2"/></svg>A slip-free surface can't be guaranteed.</li>
    <li><svg viewBox="0 0 15 13"><path d="M1 7 5 11 14 1" fill="none" stroke="#111" stroke-width="2"/></svg>Email-based snow event information and real time updates provided to customers.</li>
  </ul>

  <div class="payment-rule"></div>
  <p class="payment" style="top:685px">One payment due by october 31</p>
  <div class="pay-box" style="left:435px;top:680px;width:72px"></div>
  <p class="payment" style="top:709px">Two equal installments due by October 31 &amp; December 31</p>
  <div class="pay-box" style="left:570px;top:703px;width:72px"></div>

  <section class="sign-card">
    <h2>PLEASE SIGN AND RETURN COPY WITH PAYMENT</h2>
    <div class="sign-row"><span class="who">RIDGELINE</span><span class="line sig"></span><span class="dl">DATE</span><span class="line date"></span></div>
    <div class="sign-row"><span class="who">CUSTOMER</span><span class="line sig"></span><span class="dl">DATE</span><span class="line date"></span></div>
  </section>

  <p class="service-area">Exclusively serving Northeast Grand Rapids and suburbs</p>

  <div class="badges">
    <svg viewBox="0 0 48 52"><path d="M6 4H42V30C42 42 24 50 24 50S6 42 6 30Z" fill="var(--badge)"/></svg>
    <svg viewBox="0 0 48 52"><path d="M6 4H42V30C42 42 24 50 24 50S6 42 6 30Z" fill="var(--badge)"/></svg>
    <svg viewBox="0 0 48 52"><circle cx="24" cy="24" r="21" fill="var(--badge-dark)"/><path d="M16 40 12 51 20 47 24 44 28 47 36 51 32 40Z" fill="var(--badge-dark)"/></svg>
    <svg viewBox="0 0 48 52"><path d="M10 4H38V34C38 44 24 50 24 50S10 44 10 34Z" fill="var(--badge-dark)"/></svg>
  </div>
</main>
</body>
</html>
```